Sales Brochure- Generic Line Card 215mm x 140mm

Design a double-sided brochure similar to the attached sample. Cover Page contains a logo and theme that never changes. However, the background picture and the description text on the lower corner will be changed to advertise multiple services. Reverse-side contains Detailed Descriptive text related to the picture on Cover Page as well as Logo and Contact information for the business. Use the Ridgeline Controls website www.ridgelinecontrols.ca for theme, color and contact information. Also, use attached business card design for theme to match. Use the supplied logo. SIZE 215mm x 140mm

Font styles to use
Sans Serif

Colors

Designer to choose colors to be used in the design.

Requirements
Must have
• Look Similar to Sample Brochure but include Ridgeline Controls theme and colors

```html
<!DOCTYPE html>
<html lang="en">
<head>
<meta charset="utf-8">
<title>Ridgeline Controls – Line Card</title>
<link rel="stylesheet" href="https://fonts.googleapis.com/css2?family=Montserrat:wght@400;700;800&family=Quicksand:wght@400;500&display=swap">
<style>
  :root {
    --backdrop: #e4e4e4;
    --teal-deep: #0c4f57;
    --teal: #1a8893;
    --teal-bright: #23a3ad;
    --ink: #141414;
    --charcoal: #2a2a2a;
    --orange: #f25a0a;
    --white: #ffffff;
    --text-soft: #d6d6d6;
  }
  * { margin: 0; padding: 0; box-sizing: border-box; }
  html, body { width: 880px; height: 1200px; overflow: hidden; }
  body { background: var(--backdrop); position: relative; font-family: "Quicksand", sans-serif; }

  .card { position: absolute; left: 83px; width: 713px; height: 503px; overflow: hidden; }
  .cover { top: 71px; }
  .reverse { top: 631px; background: var(--ink); }

  .cover-photo {
    position: absolute; inset: 0;
    background:
      radial-gradient(ellipse at 72% 30%, #2f8f98 0%, rgba(20,100,108,0) 55%),
      linear-gradient(160deg, #1e7c86 0%, var(--teal-deep) 60%, #073a40 100%);
  }
  .cover-title { position: absolute; left: 66px; top: 66px; color: var(--white); font-family: "Montserrat", sans-serif; line-height: 1.1; }
  .cover-title .light { display: block; font-weight: 400; font-size: 35px; letter-spacing: -0.5px; }
  .cover-title .bold { display: block; font-weight: 800; font-size: 42px; letter-spacing: -0.5px; margin: 2px 0; }
  .cover-rule { position: absolute; left: 68px; top: 207px; width: 28px; height: 4px; background: var(--white); border-radius: 2px; }

  .brand-plate { position: absolute; left: 350px; top: 359px; width: 363px; height: 90px; background: var(--white); display: flex; align-items: center; justify-content: center; gap: 12px; }
  .brand-plate .corner { position: absolute; left: 2px; top: 2px; width: 12px; height: 12px; background: var(--teal-bright); clip-path: polygon(0 100%, 100% 0, 100% 100%); }
  .brand-mark { width: 22px; height: 22px; background: var(--teal); }
  .brand-name { font-family: "Montserrat", sans-serif; font-weight: 800; font-size: 25px; color: var(--ink); text-transform: uppercase; letter-spacing: 0.5px; }

  .reverse-photo {
    position: absolute; inset: 0;
    background:
      radial-gradient(ellipse at 45% 65%, #3a3a3a 0%, rgba(40,40,40,0) 60%),
      linear-gradient(180deg, #1a1a1a 0%, var(--charcoal) 55%, #111 100%);
  }
  .services { position: absolute; left: 66px; top: 53px; width: 560px; }
  .service { margin-bottom: 36px; }
  .service h2 { font-family: "Montserrat", sans-serif; font-weight: 700; font-size: 19px; color: var(--orange); letter-spacing: -0.3px; margin-bottom: 6px; }
  .service p { font-size: 10px; line-height: 1.3; color: var(--text-soft); font-weight: 500; }

  .contact-band { position: absolute; left: 0; top: 359px; width: 713px; height: 90px; background: var(--orange); color: var(--white); font-size: 14px; font-weight: 500; }
  .contact-item { position: absolute; display: flex; align-items: flex-start; gap: 8px; line-height: 19px; }
  .contact-item svg { width: 12px; height: 12px; margin-top: 3px; flex: none; }
  .address { left: 66px; top: 27px; }
  .phones { left: 282px; top: 27px; }
  .online { left: 448px; top: 27px; }
  .row { display: flex; align-items: center; gap: 8px; }
  .row svg { margin-top: 0; }
  .cert-badge { position: absolute; left: 560px; top: 450px; width: 83px; height: 18px; background: var(--teal); }
</style>
</head>
<body>

<section class="card cover">
  <div class="cover-photo" role="img" aria-label="Teal-toned photograph of a CNC lathe turret machining a large steel shaft"></div>
  <h1 class="cover-title">
    <span class="light">PIONEERING</span>
    <span class="bold">RESPONSIVE</span>
    <span class="light">MACHINING</span>
  </h1>
  <div class="cover-rule"></div>
  <div class="brand-plate">
    <span class="corner"></span>
    <span class="brand-mark"></span>
    <span class="brand-name">Ridgeline Controls</span>
  </div>
</section>

<section class="card reverse">
  <div class="reverse-photo" role="img" aria-label="Dark photograph of an operator's hand on a machine control keypad"></div>
  <div class="services">
    <article class="service">
      <h2>COMPUTER NUMERIC CONTROL (CNC)</h2>
      <p>CNC machining offers the most efficient method of producing steel and plastic components. The CNC is programmed using computer code to generate a digital machining process that can be repeated and precisely controlled. Repetitive tasks such as drilling, threading, and tapping are made simple using this technology.</p>
    </article>
    <article class="service">
      <h2>SWISS SCREW &amp; SMALL PARTS</h2>
      <p>Swiss machining (also known as "screw machining") is the most effective way to produce small parts like pins, screws, nuts, washers and high volume parts. The Swiss machine utilizes a simultaneous machining method</p>
    </article>
    <article class="service">
      <h2>AUTOMATION</h2>
      <p>Robotics and Automation compliment an advanced manufacturing process by adding to the productivity and efficiency of the system. Not all products benefit from automation when compared to highly skilled</p>
    </article>
  </div>

  <div class="contact-band">
    <div class="contact-item address">
      <svg viewBox="0 0 12 12" fill="none" stroke="#fff" stroke-width="1.2"><path d="M6 11 C6 11 2 7 2 4.5 A4 4 0 0 1 10 4.5 C10 7 6 11 6 11Z"/><circle cx="6" cy="4.5" r="1.4"/></svg>
      <span>4125 – 62 Street NW<br>Calgary, AB, T3B 2K7</span>
    </div>
    <div class="contact-item phones">
      <div>
        <div class="row"><svg viewBox="0 0 12 12" fill="none" stroke="#fff" stroke-width="1.2"><circle cx="6" cy="6" r="5"/><path d="M4 3.5 L5 5 L4.5 5.7 C5 6.6 5.6 7.2 6.4 7.6 L7 7 L8.5 8 L7.8 8.8 C5.6 8.6 3.4 6.4 3.2 4.2Z" fill="#fff" stroke="none"/></svg>403 555 0147</div>
        <div class="row"><svg viewBox="0 0 12 12" fill="#fff"><rect x="3" y="1" width="6" height="3"/><rect x="1" y="4.5" width="10" height="4.5" rx="1"/><rect x="3" y="8" width="6" height="3" fill="#fff" stroke="#f25a0a" stroke-width="0.8"/></svg>888 555 0192</div>
      </div>
    </div>
    <div class="contact-item online">
      <div>
        <div class="row"><svg viewBox="0 0 12 12" fill="none" stroke="#fff" stroke-width="1.1"><rect x="1" y="2.5" width="10" height="7"/><path d="M1 2.5 L6 6.5 L11 2.5"/></svg>info@ridgelinecontrols.ca</div>
        <div class="row"><svg viewBox="0 0 12 12" fill="none" stroke="#fff" stroke-width="1.1"><circle cx="6" cy="6" r="5"/><ellipse cx="6" cy="6" rx="2.2" ry="5"/><path d="M1 6 H11"/></svg>www.ridgelinecontrols.ca</div>
      </div>
    </div>
  </div>
  <div class="cert-badge" aria-hidden="true"></div>
</section>

</body>
</html>
```